CYPRUS - AYIA NAPA -LORIEL CREST HOTEL APARTMENTS NEEDS A SMART FLYER DESIGN TO ENTICE MORE GUESTS.

We are a hotel apartments located in Ayia Napa - Cyprus and we need a smart and modern brochure design to attract more people, all age and all markets for all year round vacations. The main services we would like to promote are: our hospitality, friendly atmosphere, cleanness, good and cheap food, roomy apartments and good services. In other words is " Your home away from home..."

Target Market(s)

ALL MARKETS

Industry/Entity Type

Hotel

Requirements
Must have
• TEXT AND PHOTOS
Nice to have
• " YOUR HOME AWAY FROM HOME"

```html
<!DOCTYPE html>
<html lang="en">
<head>
<meta charset="utf-8">
<title>Loriel Crest Hotel Apartments – Brochure Spread</title>
<link href="https://fonts.googleapis.com/css2?family=Cabin:wght@600;700&family=Quattrocento+Sans:wght@400;700&display=swap" rel="stylesheet">
<style>
  :root{
    --page-bg:#ece7df;
    --sand:#efe1c4;
    --sand-deep:#e6d3ae;
    --sky-panel:#a9d6e1;
    --gold:#d8c48c;
    --gold-deep:#c9b173;
    --ink:#1d1d1b;
    --teal:#1f7d8e;
    --frame:#ffffff;
  }
  *{margin:0;padding:0;box-sizing:border-box}
  html,body{width:1200px;height:900px;overflow:hidden;background:var(--page-bg)}
  .spread{position:absolute;left:72px;top:72px;width:1066px;height:755px;overflow:hidden;box-shadow:0 4px 14px rgba(0,0,0,.25);font-family:"Quattrocento Sans",sans-serif;color:var(--ink)}
  .panel{position:absolute;top:0;height:755px}
  .panel--left{left:0;width:356px;background:linear-gradient(180deg,var(--sand),var(--sand-deep))}
  .panel--middle{left:356px;width:355px;background:var(--sky-panel)}
  .panel--right{left:711px;width:355px;background:linear-gradient(160deg,#e2d09b,var(--gold) 50%,var(--gold-deep))}
  .photo{position:absolute}
  .polaroid{position:absolute;border:5px solid var(--frame);box-shadow:2px 3px 8px rgba(0,0,0,.35)}
  .heading{position:absolute;font-family:"Cabin",sans-serif;font-weight:700;color:var(--ink);line-height:1.2}
  .heading em{font-style:normal;color:var(--teal)}
  .body-copy{position:absolute;font-size:12.6px;line-height:1.68}
  .body-copy p+p{margin-top:18px}
  .body-copy strong{font-weight:700}
</style>
</head>
<body>
<main class="spread">
  <section class="panel panel--left">
    <div class="photo" role="img" aria-label="Sea cave arch over turquoise water" style="left:0;top:0;width:356px;height:283px;background:linear-gradient(180deg,#3d8fb8 0%,#6fb3c9 35%,#c9b89a 55%,#2aa0a8 80%,#1a6f8f 100%)"></div>
    <div class="polaroid" role="img" aria-label="Old stone monastery arch" style="left:20px;top:202px;width:154px;height:134px;transform:rotate(-2deg);background:linear-gradient(180deg,#8fc2e6,#c7a57a 55%,#8c8a5a)"></div>
    <div class="polaroid" role="img" aria-label="Guests with cocktails on a balcony at sunset" style="left:173px;top:180px;width:168px;height:158px;transform:rotate(4deg);background:linear-gradient(160deg,#e8a468,#b7b07a 50%,#4c5a6e)"></div>
    <h2 class="heading" style="left:29px;top:378px;width:296px;font-size:15px">Situated only 45 km away from Larnaca International Airport, Loriel Crest is an ideal blend of <em>peace, convenience, and comfort.</em></h2>
    <div class="body-copy" style="left:29px;top:472px;width:300px">
      <p>A place where local culture welcomes travelers from far and away. Nestled in an ideally unique location, just outside the busy bar strip of Ayia Napa but only 5 minutes away from the town centre and all the main seaside attractions, it lets visitors decide the way their day will evolve. Whether you feel cosmopolitan or on a lay down mood, Loriel Crest has you covered.</p>
      <p>Mr. Themis and his family manage the place themselves, adapting to the individual preferences of almost every traveler. Service and quality is their self driving motto for success.</p>
    </div>
  </section>

  <section class="panel panel--middle">
    <h1 class="heading" style="left:24px;top:32px;width:310px;font-size:15px">Loriel Crest is a <em>year-round resort</em> for families, couples and individuals alike!</h1>
    <div class="photo" role="img" aria-label="Couple relaxing in an apartment living room" style="left:9px;top:104px;width:338px;height:142px;background:linear-gradient(90deg,#b8bfcf,#e9e6e2 50%,#6f86b0)"></div>
    <div class="photo" role="img" aria-label="Guests by the hotel pool" style="left:9px;top:246px;width:168px;height:165px;border-top:2px solid #fff;border-right:2px solid #fff;background:linear-gradient(180deg,#d9d3c5,#6fb0c8 60%,#2f7fa3)"></div>
    <div class="photo" role="img" aria-label="Guest reading in the hotel garden" style="left:177px;top:246px;width:170px;height:165px;border-top:2px solid #fff;background:linear-gradient(180deg,#cfd6d8,#5d8a3e 45%,#3a5a2a)"></div>
    <h2 class="heading" style="left:30px;top:431px;width:290px;font-size:15px">The Loriel Crest Hotel Apartments resort presents <em>39 comfortable guestrooms</em> that are spacious and renovated.</h2>
    <div class="body-copy" style="left:30px;top:518px;width:300px">
      <p>All rooms are fully air-conditioned and heated featuring a fully equipped kitchen, living room, WC, satellite TV and private balcony.</p>
    </div>
  </section>

  <section class="panel panel--right">
    <div class="photo" role="img" aria-label="Hotel building and outdoor swimming pool" style="left:0;top:0;width:355px;height:273px;background:linear-gradient(180deg,#8fc1e8 0%,#f1ead8 25%,#efe2c8 55%,#3f8ec9 75%,#1f5fa8 100%)"></div>
    <div class="polaroid" role="img" aria-label="Sunset over the sea" style="left:36px;top:192px;width:152px;height:160px;transform:rotate(-3deg);background:linear-gradient(180deg,#3c5a85,#e7a46f 45%,#7b8fa8 60%,#2d4d6e)"></div>
    <div class="polaroid" role="img" aria-label="Guest at the pool bar" style="left:168px;top:226px;width:172px;height:170px;transform:rotate(5deg);background:linear-gradient(160deg,#9aa6a0,#d7a94a 50%,#6b4b36)"></div>
    <div class="body-copy" style="left:34px;top:418px;width:295px;text-align:justify;line-height:1.62">
      <p>When it comes to <strong>guest entertainment</strong>, the hotel provides an <strong>upbeat environment</strong> that includes among others, a large outdoor swimming pool surrounded by terrace, sun beds, umbrellas and a separate children's pool. Guests at the pool bar can enjoy good food and drinks accompanied by a wide selection of outdoor activities that include water polo, pool table, dart and video games. Sport coverage is also at hand with the use of a large outside TV screen.</p>
    </div>
  </section>

  <div class="polaroid" role="img" aria-label="Modern bathroom" style="left:368px;top:612px;width:152px;height:150px;transform:rotate(-2deg);background:linear-gradient(160deg,#f1f3f4,#cfd8dc 60%,#7fa9ad)"></div>
  <div class="polaroid" role="img" aria-label="Apartment living and dining area" style="left:523px;top:622px;width:136px;height:140px;background:linear-gradient(180deg,#f3f2ef,#c9c3b2 55%,#5a6ea3)"></div>
  <div class="polaroid" role="img" aria-label="Guests in a bright bedroom" style="left:660px;top:612px;width:156px;height:150px;transform:rotate(-4deg);background:linear-gradient(160deg,#7c8cad,#e7d7c0 50%,#b39a78)"></div>
  <div class="polaroid" role="img" aria-label="Apartment lounge with blue sofas" style="left:818px;top:625px;width:162px;height:140px;transform:rotate(3deg);background:linear-gradient(180deg,#f2f2f0,#c8c8c4 55%,#34508f)"></div>
</main>
</body>
</html>
```